Stationery for new photography studio
Flyer, Gift Certificate, Business Card, headed paper, CD label and case cover
Please note the change in email address
studio@brightferndesigns.at
Dear sir,
Thanks for your feedback.
#100 is brilliant
I really like #97. I love the colours from the photos. I like the new business cards. Could you combine the concepts in the business cards from #94 #96 #97
temp web address
http://brightferndesigns.snapvault-host.com/
#89 every thing looks great. A few comments:
1) The business cards - I like the logo side however the information side I prefer earlier designs where you used one block colour ie- #87 or #49. I'm still not sure about this side.
2) The dark black logo square on the paper looks too bold.
Great work. Thanks a lot.
Please check the newly uploaded files.
PANTONES:
Blue: 310 C
Brown: 409 C
Pink: 211 C
Gray: 424 C
FONTS:
Petra: Gotham Medium
Valkenor: Gotham Book
Tagline: Gotham Book
Signature: Custom made
I think I prefer the logo in #52 where it is slightly off the page than #70 where it is completely visible.
I like #70, it's sophisticated however the colour scheme is starting depart from the original and from the style of my work, which I think is not so heavy.
If you have any change or better suggestions please let me know.
Thank you.
#61 - #64 I'm not sure if the dots down the sides are necessary.
My website is down. But I'LL let you know when it's back up so you can take a look at some more pictures. I love the use of them in your designs. So excited by what I'm seeing. Thanks for your work so far.
#57. I love it. Everything adds up perfectly. Not sure about the font. It's a bit clumsy. I'd like something sharper and sleeker.
Great direction.
Does this work for A6
A CD disk is 120 mm in diameter (60 mm radius), with a hole 15 mm diameter (7.5 mm radius)
I'm looking on google for CD dimensions. So far I've found the case cover dimensions:
CD Cover Size Specifications for Printing
The finished dimensions for the outside of printed CD covers are 4.724 inches square. Many printed designs include bleed. The "bleed area" is an extra 1/8" of space for design elements or backgrounds to extend beyond the finished size of your piece. A CD cover with bleeds is printed slightly oversized (4.974 inches square) and then cut down to size, giving the appearance that the printing "bleeds" off the edge of the cover rather than having a white border.
Really like the direction of #51 and #52. Re. #55 I prefer the designs where all embellishments or lines are relevant. What I mean by this is that the curve does not tie in anywhere. It's an additional form that is not part of the logo.
#61 and #62 are great. Can you show me some alternative fonts for the 15% and the brightferndesigns.at
This is fun project! What size should be the CD label be? I am not too sure!
#36 with black background?
I'd be interested to see #34 with black replacing the pink.
I have uploaded information to be included in the flyers and gift certificate.
Please look at my photos to understand my style
http://www.facebook.com/BrightFern.Designs?sk=app_274930158846320

```html
<!DOCTYPE html>
<html lang="de">
<head>
<meta charset="utf-8">
<title>Petra Valkenor – Business Card</title>
<link rel="stylesheet" href="https://fonts.googleapis.com/css2?family=Montserrat:wght@400;500&family=Open+Sans:wght@400;700&display=swap">
<style>
  :root {
    --page-bg: #eeeae5;
    --card-bg: #ffffff;
    --pink: #f08fb0;
    --pink-strip: #f29ab9;
    --divider: #3f3a3c;
    --gray-text: #6d6466;
    --ink: #2c2a2b;
  }
  * { margin: 0; padding: 0; box-sizing: border-box; }
  html, body {
    width: 1200px; height: 965px; overflow: hidden;
    background: var(--page-bg);
  }
  .business-card {
    position: absolute;
    left: 240px; top: 235px;
    width: 775px; height: 445px;
    background: var(--card-bg);
    border-radius: 30px;
    overflow: hidden;
    box-shadow: 0 6px 18px rgba(0,0,0,0.18);
  }
  .side-strip {
    position: absolute; left: 0; top: 0;
    width: 73px; height: 100%;
    background: var(--pink-strip);
  }
  .side-divider {
    position: absolute; left: 76px; top: 0;
    width: 3px; height: 100%;
    background: var(--divider);
  }
  .brand {
    position: absolute; left: 107px; top: 40px;
    width: 470px;
    text-align: center;
  }
  .brand-square {
    display: block;
    width: 70px; height: 70px;
    margin: 0 auto 30px;
    background: var(--pink);
    border-radius: 6px;
  }
  .brand-name {
    font-family: "Montserrat", sans-serif;
    font-weight: 400;
    font-size: 38px;
    letter-spacing: 5px;
    color: var(--gray-text);
    white-space: nowrap;
  }
  .contact-list {
    position: absolute; left: 0; top: 280px;
    list-style: none;
  }
  .contact-item {
    display: flex; align-items: center;
    height: 31.5px;
  }
  .contact-icon {
    width: 73px; display: flex; justify-content: center;
  }
  .contact-icon svg { width: 20px; height: 20px; fill: #fff; }
  .contact-text {
    margin-left: 13px;
    font-family: "Open Sans", sans-serif;
    font-size: 21px;
    color: var(--ink);
    white-space: nowrap;
  }
  .holder-name {
    position: absolute; left: 500px; top: 312px;
    width: 235px; text-align: center;
    font-family: "Open Sans", sans-serif;
    font-weight: 700;
    font-size: 30px;
    color: var(--pink);
    white-space: nowrap;
  }
</style>
</head>
<body>
  <div class="business-card">
    <div class="side-strip"></div>
    <div class="side-divider"></div>

    <div class="brand">
      <span class="brand-square"></span>
      <div class="brand-name">Petra Valkenor</div>
    </div>

    <ul class="contact-list">
      <li class="contact-item">
        <span class="contact-icon">
          <svg viewBox="0 0 20 20" aria-hidden="true"><path d="M10 2 L19 10 H16 V18 H12 V13 H8 V18 H4 V10 H1 Z"/></svg>
        </span>
        <span class="contact-text">Lindengasse 24/7&nbsp;&nbsp;1070 Wien</span>
      </li>
      <li class="contact-item">
        <span class="contact-icon">
          <svg viewBox="0 0 20 20" aria-hidden="true"><path d="M5 2 L8 6 L6 8 C7 11 9 13 12 14 L14 12 L18 15 L16 18 C9 18 2 11 2 4 Z"/></svg>
        </span>
        <span class="contact-text">06641837526</span>
      </li>
      <li class="contact-item">
        <span class="contact-icon">
          <svg viewBox="0 0 20 20" aria-hidden="true"><circle cx="10" cy="6" r="4"/><path d="M3 18 C3 12 17 12 17 18 Z"/></svg>
        </span>
        <span class="contact-text">Petra@Valkenor.at</span>
      </li>
      <li class="contact-item">
        <span class="contact-icon">
          <svg viewBox="0 0 20 20" aria-hidden="true"><path d="M10 1 A9 9 0 1 0 16 16 L14.6 14.6 A7 7 0 1 1 17 10 V11 A1.5 1.5 0 0 1 14 11 V6 H12 V6.8 A4 4 0 1 0 12.6 13 A3.5 3.5 0 0 0 19 11 V10 A9 9 0 0 0 10 1 Z M10 8 A2 2 0 1 1 10 12 A2 2 0 1 1 10 8 Z"/></svg>
        </span>
        <span class="contact-text">www.BrightFernDesigns.at</span>
      </li>
    </ul>

    <div class="holder-name">Petra Valkenor</div>
  </div>
</body>
</html>
```